Crust Harbor wants to rebrand thier Menu/Image

Looking to re brand to a more casual hip vibe. I was thinking a simple "sketch feel" Kraft Paper Menu. I have uploaded some inspirational images. The menu will serve as a jumping off point to re brand our web presence. (www.crustharbor.org). and eventually our decor. Take a look at our web page for a feel of what we do and who we are

Target Market(s)

Pizza Take Out Quick Serve Customers. Family Restaurant

Requirements
Must have
• -Adaptable to become in house menu.
• - Use our existing logo
• -playful, fun, hip not to sophisticated
• --Use "Traditional Quality Control Image". (three guys)
• Cool (tone) Kraft Paper. Black/Sepia text. Touches of "Pizza Sauce" red

```html
<!DOCTYPE html>
<html lang="en">
<head>
<meta charset="utf-8">
<title>Crust Harbor – Goodies &amp; Beverages Menu Panel</title>
<link href="https://fonts.googleapis.com/css2?family=Rye&family=IM+Fell+English&family=Oswald:wght@500;600&display=swap" rel="stylesheet">
<style>
  :root {
    --backdrop: #e9e6e1;
    --kraft-light: #ecd9a8;
    --kraft-mid: #dcc08a;
    --kraft-edge: #b8955b;
    --sauce-red: #b3202a;
    --sauce-dark: #5e0f12;
    --ink: #2a1c10;
    --sepia-light: #e4cfa0;
    --sepia-dark: #4a3218;
  }
  html, body {
    margin: 0;
    width: 963px;
    height: 1200px;
    overflow: hidden;
    background: var(--backdrop);
  }
  .menu-panel {
    position: absolute;
    left: 284px;
    top: 30px;
    width: 395px;
    height: 1140px;
    box-sizing: border-box;
    padding: 48px 30px 0 34px;
    background:
      radial-gradient(ellipse at 50% 45%, var(--kraft-light) 0%, var(--kraft-mid) 70%, var(--kraft-edge) 100%);
    color: var(--ink);
    font-family: "IM Fell English", Georgia, serif;
    box-shadow: 0 4px 14px rgba(0,0,0,0.18);
    border-right: 3px solid var(--sauce-red);
  }
  .section-title {
    margin: 0;
    font-family: "Rye", Georgia, serif;
    font-weight: 400;
    color: var(--sauce-red);
    text-shadow: 2px 2px 0 var(--sauce-dark);
    line-height: 1;
    letter-spacing: 1px;
  }
  .section-title--goodies { font-size: 52px; }
  .section-title--beverages { font-size: 52px; margin-top: 30px; }
  .section-title--locations { font-size: 52px; }
  .menu-list { list-style: none; margin: 18px 0 0; padding: 0; font-size: 14.5px; line-height: 1.1; }
  .menu-item { margin-bottom: 12px; }
  .menu-item__name { text-transform: uppercase; }
  .menu-item__price { margin-left: 8px; }
  .menu-item__desc { display: block; font-size: 14px; }
  .menu-item--short { margin-bottom: 0; }
  .beverage-note { margin: 6px 0 0; font-size: 14.5px; line-height: 1.1; }
  .beverage-art {
    display: block;
    margin: 18px auto 0;
    width: 300px;
    height: 350px;
    border-radius: 46% 40% 44% 38%;
    background: radial-gradient(ellipse at 45% 50%, var(--sepia-light) 0%, #b89460 50%, var(--sepia-dark) 85%, rgba(74,50,24,0) 100%);
  }
  .locations { position: absolute; left: 34px; right: 30px; top: 860px; }
  .location-list { list-style: none; margin: 18px 0 0; padding: 0; }
  .location { margin-bottom: 10px; }
  .location__name {
    display: block;
    font-family: "Oswald", "Arial Narrow", sans-serif;
    font-weight: 600;
    font-size: 17px;
    color: var(--sauce-red);
    text-transform: uppercase;
    letter-spacing: 0.5px;
  }
  .location__detail {
    display: block;
    font-family: "Oswald", "Arial Narrow", sans-serif;
    font-weight: 500;
    font-size: 13.5px;
    text-transform: uppercase;
    color: var(--ink);
  }
  .social {
    position: absolute;
    right: 28px;
    bottom: 28px;
    display: flex;
    align-items: center;
    gap: 8px;
  }
  .social__square { width: 40px; height: 40px; background: var(--sauce-red); }
  .social__name {
    font-family: "Oswald", "Arial Narrow", sans-serif;
    font-weight: 600;
    font-size: 15px;
    color: var(--sauce-red);
    text-transform: uppercase;
  }
</style>
</head>
<body>
  <main class="menu-panel">
    <section class="goodies">
      <h2 class="section-title section-title--goodies">Goodies</h2>
      <ul class="menu-list">
        <li class="menu-item">
          <span class="menu-item__name">Cinammon Knots</span><span class="menu-item__price">$4</span>
          <span class="menu-item__desc">our classic knots loaded with butter, cinnamon &amp; sugar, served with icing</span>
        </li>
        <li class="menu-item">
          <span class="menu-item__name">Silly Sweet Cinnamon Sticks</span><span class="menu-item__price">$4</span>
          <span class="menu-item__desc">our homemade dough with a sweet blend of cinnamon and sugar, baked to perfection &amp; topped with icing</span>
        </li>
        <li class="menu-item menu-item--short"><span class="menu-item__name">Cannoli</span><span class="menu-item__price">$3</span></li>
        <li class="menu-item menu-item--short"><span class="menu-item__name">Cookies</span><span class="menu-item__price">$2</span></li>
      </ul>
    </section>

    <section class="beverages">
      <h2 class="section-title section-title--beverages">Beverages</h2>
      <p class="beverage-note">SOFT DRINKS<br>we proudly serve Fizzwell products, flavors vary</p>
      <div class="beverage-art" role="img" aria-label="Sepia sketch of a glass of cola with ice and a straw, with two cookies beside it"></div>
    </section>

    <section class="locations">
      <h2 class="section-title section-title--locations">Locations</h2>
      <ul class="location-list">
        <li class="location"><span class="location__name">Harbor Point</span><span class="location__detail">12 Dockside Ave | 555.0142</span></li>
        <li class="location"><span class="location__name">Cedar Bluff</span><span class="location__detail">480 Lantern Rd | 555.0187</span></li>
        <li class="location"><span class="location__name">Millbrook</span><span class="location__detail">31 Quarry St | 555.0163</span></li>
      </ul>
    </section>

    <div class="social">
      <span class="social__square"></span>
      <span class="social__name">Crust Harbor</span>
    </div>
  </main>
</body>
</html>
```